Clausewise - Training I Consulting I Review - Related to Contracts/Agreements

We provide legal services, we need a plattform to book video online trainings or local trainings classes and appointments (with calendar feature to select date and see availability at screen), payment over internet, legal document creation over webpage, videos will be produces in the next 3 - 4 moths so this is a place holder item. Participants for the Online trainings shall have a login in area with secured password. Appointments for local trainings and Consulting. Consider Outline in file attached. I can send you also a video with more explanation regarding the purpose.

Target Market(s)

Startup/scale up Software companies that intent to have an international business and need help with their contracts, to sell their products. Sales persons.

Industry/Entity Type

Legal

Coding

Coded - Design and coding required

Number of Pages Required

5+ page

Font styles to use
Serif
Sans Serif

Colors
000000
eeeeee
f5f5f5
ffffff
f8fcfd
3277b5
ecf7fb
cadf82
86cfc6

Requirements
Must have
• See file clausewise attached with outline. Moreover see here first starting point: https://tomas-vendrell.pagebuildr.example/mysite-1 . Main inspiration comes from www.advisoryhub.example from the log in area, see the outline in the file attached with the screen shots. At the end I need someone who can draft the full webpage and maintain it for a yearly fee. It must be simple and well structured layout. Lean. 1st landing page shall not scroll, 2 landing page only a little to see the testimonials and foster of page. There should be a Progress Bar to indicate the booking/selection process. Calendar booking. Easy fast booking.
• I like the colour mix, the feeling and the easy structor of:
• https://www.artmarket.example/design/6374387or
• https://www.artmarket.example/design/6372391 or https://www.artmarket.example/design/6374366
• https://www.vendorgrid.example/en/web-design/belgium-be
• https://www.artmarket.example/design/5896857
• https://www.artmarket.example/design/5902173
• https://www.artmarket.example/design/17197349
• https://www.artmarket.example/design/5464461
• https://www.artmarket.example/design/7180908
Nice to have
• page for evaluation and interview, see outline attached in the file with screen shots. Document upload.
Should not have
• many pictures, long scroll down pages on the 1st and 2nd ladding pages, many colours and forms. No need for news letter, search field, no need for links to Chatterly and other social media (except workNet).

```html
<!DOCTYPE html>
<html lang="en">
<head>
<meta charset="utf-8">
<title>Clausewise – Services</title>
<link href="https://fonts.googleapis.com/css2?family=Marcellus&family=Nunito+Sans:wght@400;600&display=swap" rel="stylesheet">
<style>
  :root {
    --ink: #000000;
    --paper: #ffffff;
    --mist: #f4f4f4;
    --slate-top: #56606a;
    --slate-mid: #2f353d;
    --slate-deep: #22262c;
    --body-grey: #555555;
    --footer-rule: #3a3a3a;
    --serif: "Marcellus", Georgia, serif;
    --sans: "Nunito Sans", Arial, sans-serif;
  }
  * { margin: 0; padding: 0; box-sizing: border-box; }
  html, body { width: 1045px; height: 1200px; overflow: hidden; background: var(--paper); }
  body { position: relative; font-family: var(--serif); color: var(--ink); }

  .services {
    position: absolute; left: 0; top: 0; width: 1045px; height: 653px;
    background: radial-gradient(ellipse 70% 45% at 50% 0%, var(--slate-top) 0%, var(--slate-mid) 55%, var(--slate-deep) 100%);
  }
  .section-title {
    position: absolute; left: 0; width: 100%; text-align: center;
    font-family: var(--serif); font-weight: 400; font-size: 29px; letter-spacing: 0.5px;
  }
  .services .section-title { top: 50px; color: var(--paper); }

  .service-card {
    position: absolute; top: 124px; width: 251px; height: 457px; background: var(--paper);
  }
  .service-photo { position: absolute; left: 0; top: 0; width: 100%; height: 178px; }
  .photo-training { background: linear-gradient(135deg, #3b3328 0%, #8a7c6a 45%, #2c3a6a 100%); }
  .photo-consulting { background: linear-gradient(120deg, #1e2a55 0%, #b9b2a8 50%, #24305c 100%); }
  .photo-design { background: linear-gradient(135deg, #d8d6d2 0%, #a9a39b 50%, #4a4e52 100%); }

  .service-name {
    position: absolute; top: 200px; width: 100%; text-align: center;
    font-size: 15.5px; font-weight: 400; letter-spacing: 0.3px;
  }
  .service-rule {
    position: absolute; top: 352px; left: 100px; width: 50px; height: 2px; background: var(--ink);
  }
  .service-card .service-rule { top: 228px; }
  .service-text {
    position: absolute; top: 248px; left: 30px; width: 191px; text-align: center;
    font-size: 10px; line-height: 16px; color: var(--body-grey);
  }
  .service-button {
    position: absolute; top: 380px; left: 33px; width: 185px; height: 45px;
    border: 1px solid var(--ink); text-align: center; line-height: 43px;
    font-size: 14.5px; color: var(--ink);
  }

  .testimonials .section-title { top: 712px; color: var(--ink); font-size: 24px; }
  .testimonial {
    position: absolute; top: 806px; width: 397px; height: 189px; background: var(--mist);
  }
  .portrait {
    position: absolute; top: -13px; left: 21px; width: 108px; height: 125px;
    border: 6px solid var(--ink);
  }
  .portrait-fill { width: 100%; height: 100%; }
  .portrait-warm { background: linear-gradient(180deg, #cfc6bd 0%, #8a5a3e 60%, #e8e2dc 100%); }
  .portrait-cool { background: linear-gradient(180deg, #d9dde0 0%, #5a4a40 55%, #3a4658 100%); }
  .name-tag {
    position: absolute; left: 129px; top: 14px;
  }
  .person-name {
    position: absolute; left: 141px; top: 22px; font-family: var(--sans);
    font-size: 10px; font-weight: 600; color: var(--ink);
  }
  .person-role {
    position: absolute; left: 141px; top: 47px; font-family: var(--sans);
    font-size: 8px; font-weight: 600; color: var(--paper);
  }
  .rating { position: absolute; left: 142px; top: 77px; }
  .quote {
    position: absolute; left: 142px; top: 103px; width: 232px;
    font-family: var(--sans); font-size: 9.3px; line-height: 14.5px; color: #333333;
  }

  .site-footer {
    position: absolute; left: 0; top: 1064px; width: 1045px; height: 136px; background: var(--ink);
  }
  .footer-link {
    position: absolute; font-family: var(--serif); font-size: 9px; color: var(--paper);
  }
  .footer-rule {
    position: absolute; left: 0; top: 94px; width: 100%; height: 1px; background: var(--footer-rule);
  }
  .copyright {
    position: absolute; top: 109px; width: 100%; text-align: center;
    font-family: var(--sans); font-size: 8.5px; color: var(--paper);
  }
</style>
</head>
<body>

<section class="services">
  <h1 class="section-title">CHOOSE YOUR SERVICE</h1>

  <article class="service-card" style="left:126px;">
    <div class="service-photo photo-training" role="img" aria-label="Photo: people taking notes at a desk with laptop and coffee cup"></div>
    <h2 class="service-name">CONTRACT TRAINING</h2>
    <div class="service-rule"></div>
    <p class="service-text">We know that training is a key component of attracting and retaining engaged employees. Choose training contract that will work with you to put together the high-quality educational programs you require, tailored to your needs, on your schedule</p>
    <div class="service-button">SEARCH</div>
  </article>

  <article class="service-card" style="left:397px;">
    <div class="service-photo photo-consulting" role="img" aria-label="Photo: business meeting between three professionals"></div>
    <h2 class="service-name">CONTRACT CONSULTING</h2>
    <div class="service-rule"></div>
    <p class="service-text">We provide specialized services to Government contractors. Our professionals have the related practical experience to assist companies in successfully meeting the increasing challenges of the highly regulated, closely scrutinized, and intensely competitive</p>
    <div class="service-button">SEARCH</div>
  </article>

  <article class="service-card" style="left:669px;">
    <div class="service-photo photo-design" role="img" aria-label="Photo: team reviewing printed layouts on a table"></div>
    <h2 class="service-name">CONTRACT DESIGN</h2>
    <div class="service-rule"></div>
    <p class="service-text">Although transaction lawyers spend much time drafting contracts and related documents, they can contribute very significant value by designing transactions. Transactions should be tailored to the goals and circumstances of each set of parties so it will avoid copyright issues.</p>
    <div class="service-button">SEARCH</div>
  </article>
</section>

<section class="testimonials">
  <h2 class="section-title">TESTIMONIAL</h2>

  <article class="testimonial" style="left:114px;">
    <div class="portrait"><div class="portrait-fill portrait-warm" role="img" aria-label="Portrait photo of the client"></div></div>
    <svg class="name-tag" width="140" height="52" viewBox="0 0 140 52">
      <polygon points="0,0 127,0 117,27 0,27" fill="#ffffff"/>
      <polygon points="0,27 107,27 97,52 0,52" fill="#000000"/>
    </svg>
    <div class="person-name">MARTA OLSEN</div>
    <div class="person-role">FOUNDER &amp; CEO</div>
    <svg class="rating" width="104" height="18" viewBox="0 0 104 18">
      <defs><path id="star-a" d="M9 0.8l2.4 5.6 6 .5-4.6 4 1.4 6-5.2-3.2-5.2 3.2 1.4-6-4.6-4 6-.5z"/></defs>
      <use href="#star-a" x="0" fill="#000"/>
      <use href="#star-a" x="21" fill="#000"/>
      <use href="#star-a" x="42" fill="#000"/>
      <use href="#star-a" x="63" fill="#000"/>
      <use href="#star-a" x="84" fill="none" stroke="#000" stroke-width="0.9"/>
    </svg>
    <p class="quote">Lorem ipsum dolor sit amet, consectetur adipisicing elit, sed do eiusmod tempor incididunt ut labore et dolore magna aliqua.&nbsp; Lorem ipsum dolor sit amet, consectetur adipisicing elit</p>
  </article>

  <article class="testimonial" style="left:532px;">
    <div class="portrait"><div class="portrait-fill portrait-cool" role="img" aria-label="Portrait photo of the client"></div></div>
    <svg class="name-tag" width="140" height="52" viewBox="0 0 140 52">
      <polygon points="0,0 127,0 117,27 0,27" fill="#ffffff"/>
      <polygon points="0,27 107,27 97,52 0,52" fill="#000000"/>
    </svg>
    <div class="person-name">ELIAS BRANDT</div>
    <div class="person-role">HEAD OF IDEA</div>
    <svg class="rating" width="104" height="18" viewBox="0 0 104 18">
      <defs><path id="star-b" d="M9 0.8l2.4 5.6 6 .5-4.6 4 1.4 6-5.2-3.2-5.2 3.2 1.4-6-4.6-4 6-.5z"/></defs>
      <use href="#star-b" x="0" fill="#000"/>
      <use href="#star-b" x="21" fill="#000"/>
      <use href="#star-b" x="42" fill="#000"/>
      <use href="#star-b" x="63" fill="#000"/>
      <use href="#star-b" x="84" fill="none" stroke="#000" stroke-width="0.9"/>
    </svg>
    <p class="quote">Lorem ipsum dolor sit amet, consectetur adipisicing elit, sed do eiusmod tempor incididunt ut labore et dolore magna aliqua.&nbsp; Lorem ipsum dolor sit amet, consectetur adipisicing elit</p>
  </article>
</section>

<footer class="site-footer">
  <span class="footer-link" style="left:125px; top:24px;">EVALUATION</span>
  <span class="footer-link" style="left:125px; top:48px;">MARKET FEEDBACK</span>
  <span class="footer-link" style="left:329px; top:24px;">STUDENTS</span>
  <span class="footer-link" style="left:329px; top:48px;">TEMPLATES</span>
  <span class="footer-link" style="left:534px; top:24px;">POLICIES</span>
  <span class="footer-link" style="left:534px; top:48px;">TOOLS</span>
  <span class="footer-link" style="left:737px; top:24px;">TEAM</span>
  <span class="footer-link" style="left:737px; top:48px;">CONTACT</span>
  <div class="footer-rule"></div>
  <p class="copyright">©2018 Clausewise.com</p>
</footer>

</body>
</html>
```